Website Design for Law Firm

I need a website for my law firm. The firm name is Brantley Legal PLLC. It would be helpful if the site included a logo (font treatment) on the website such as the logo on rvcounsel.com. Note: the graphic is not necessary. 

The site should be somewhat conservative but modern. You can view brantleypllc.com to see the type of pages I want. Please don't allow your creativity to be limited by the current design because I'm not a website designer which is why I am outsourcing this job. The site should not be a complete picture as currently displayed on the current website.

More Guidance:
I like the design of the following template: http://www.layoutforge.com/website-templates/14982.html?tab=32 The layout I want would be similar to that template. I'm not a huge fan of their color scheme. I would prefer blue instead of orange. Their should be four buttons in the navigation bar instead of six: Firm, Attorney, Practices, Contacts. The navigation bar should be below the law firm name (logo).

Finally, the firm name is Brantley Legal PLLC. I would like to the firm name written similar to the rvcounsel.com website. Brantley and Law would be different colors and PLLC would be written vertically.

Target Market(s)

Young Professionals and Startup Companies

Industry/Entity Type

Law Firm

Requirements
Must have
• Home page, attorney profile page, disclaimer page, attorney advertising page, contact page, practice page(s). The contact page needs a input field(s) that could submit name/subject/message to my email address.
Nice to have
• A (google) map that will show the location of my office on the contact page. 
• A link to an RSS feed that displays legal articles. Similar to the one on the ostrandlegal.com home page. However, it should not be on the home page.

```html
<!DOCTYPE html>
<html lang="en">
<head>
<meta charset="utf-8">
<title>Brantley Legal PLLC — Attorney at Law</title>
<link rel="stylesheet" href="https://fonts.googleapis.com/css2?family=Arimo:wght@400;700&family=Archivo+Narrow:wght@400&family=Open+Sans:wght@600&family=Tinos:wght@400&display=swap">
<style>
  :root {
    --navy: #0c0f63;
    --hero-grey: #7d7d7d;
    --top-strip: #d4d6da;
    --nav-bg: #fbfbfb;
    --rule-grey: #a4a7ab;
    --heading: #3a3a3a;
    --body-text: #111111;
    --link: #0c0f4a;
    --footer-bg: #dcdee1;
    --footer-text: #474747;
    --white: #ffffff;
  }
  * { margin: 0; padding: 0; box-sizing: border-box; }
  html, body { width: 1200px; height: 1200px; overflow: hidden; background: var(--white); }
  body { position: relative; font-family: "Arimo", Arial, sans-serif; color: var(--body-text); }

  .hero { position: absolute; left: 0; top: 0; width: 1200px; height: 365px; background: var(--hero-grey); }
  .hero__strip { position: absolute; left: 525px; top: 0; width: 675px; height: 37px; background: linear-gradient(#e6e7e9, var(--top-strip)); }
  .hero__tagline { position: absolute; left: 60px; top: 212px; font-size: 31px; color: var(--white); letter-spacing: 0.5px; }
  .hero__portrait { position: absolute; left: 780px; top: 37px; width: 420px; height: 328px; background: linear-gradient(90deg, #9c9c9c 0%, #6a6a6a 40%, #3a3a3a 70%, #8a8a8a 100%); }

  .brand { position: absolute; left: 0; top: 0; width: 525px; height: 155px; background: var(--navy); }
  .brand__name { position: absolute; left: 44px; top: 34px; font-family: "Open Sans", Arial, sans-serif; font-weight: 600; font-size: 42px; letter-spacing: -1.5px; color: var(--white); white-space: nowrap; }
  .brand__rule { position: absolute; left: 42px; top: 101px; width: 458px; height: 1px; background: var(--white); }
  .brand__tagline { position: absolute; left: 42px; width: 458px; top: 110px; text-align: center; font-size: 18px; color: var(--white); letter-spacing: 0.5px; }

  .main-nav { position: absolute; left: 0; top: 365px; width: 1200px; height: 100px; background: var(--nav-bg); border-bottom: 4px solid var(--rule-grey); }
  .main-nav a { position: absolute; top: 36px; transform: translateX(-50%); font-family: "Tinos", "Times New Roman", serif; font-size: 25px; color: #111; text-decoration: none; }

  .section-title { position: absolute; font-family: "Tinos", "Times New Roman", serif; font-weight: 400; font-size: 26px; color: var(--heading); letter-spacing: 0.5px; }

  .welcome__text { position: absolute; left: 62px; top: 570px; width: 640px; font-family: "Archivo Narrow", "Arial Narrow", sans-serif; font-size: 15.4px; line-height: 22.7px; white-space: nowrap; }
  .text-link { position: absolute; font-size: 18px; color: var(--link); text-decoration: none; }

  .practice-list { position: absolute; left: 62px; top: 827px; list-style: none; font-size: 18.5px; line-height: 27.3px; }

  .news__image { position: absolute; left: 711px; width: 443px; }
  .news__image--banner { top: 588px; height: 112px; background: linear-gradient(90deg, #0b0e5e 0%, #141875 55%, #3a3d86 100%); }
  .news__image--papers { top: 798px; height: 114px; background: linear-gradient(180deg, #d9d9d9 0%, #bdbdbd 50%, #5a5a5a 100%); }
  .news__text { position: absolute; left: 711px; width: 445px; font-size: 18.5px; line-height: 22.5px; white-space: nowrap; }

  .site-footer { position: absolute; left: 0; top: 1074px; width: 1200px; height: 126px; background: var(--footer-bg); border-top: 2px solid #eceded; }
  .site-footer p { position: absolute; top: 50px; width: 1200px; text-align: center; font-size: 20px; color: var(--footer-text); }
  .site-footer .copy { font-size: 24px; margin-right: 10px; }
</style>
</head>
<body>
  <header class="hero">
    <div class="hero__strip"></div>
    <div class="hero__portrait" role="img" aria-label="Black and white portrait of the attorney in a suit seated at a desk"></div>
    <p class="hero__tagline">BE CONFIDENT IN YOUR FUTURE</p>
    <div class="brand">
      <span class="brand__name">BRANTLEY LEGAL PLLC</span>
      <div class="brand__rule"></div>
      <span class="brand__tagline">ATTORNEY AT LAW</span>
    </div>
  </header>

  <nav class="main-nav">
    <a href="#" style="left:175px">Firm</a>
    <a href="#" style="left:457px">Attorney</a>
    <a href="#" style="left:747px">Practices</a>
    <a href="#" style="left:1047px">Contacts</a>
  </nav>

  <section class="welcome">
    <h2 class="section-title" style="left:60px; top:533px">WELCOME</h2>
    <p class="welcome__text">For more than a decade, our Law Firm has been providing skilled legal services to clients from across the<br>United States and around the world. If you have visited our site because you need a lawyer, you will<br>immediately realize you need search no further. At the Law Offices, we give clients personal attention and<br>aggressive representation. Our law firm provide a variety of legal services to a deverse and<br>constantly expanding clientage. Our lawyers will represent clients in bankruptsy, business, civil rights,<br>construction, consumer, contracts, criminal, family, insurance, immigration, taxation, will and probate and<br>many other cases.</p>
    <a class="text-link" href="#" style="left:582px; top:732px">Read More</a>
  </section>

  <section class="practice-areas">
    <h2 class="section-title" style="left:58px; top:792px">PRACTICE AREAS</h2>
    <ul class="practice-list">
      <li>Business Law</li>
      <li>Civil Litigation</li>
      <li>Estate Planning</li>
      <li>Family Law</li>
    </ul>
  </section>

  <section class="news">
    <h2 class="section-title" style="left:711px; top:533px">NEWS</h2>
    <div class="news__image news__image--banner" role="img" aria-label="In the news banner with folded newspaper and coffee cup on navy"></div>
    <p class="news__text" style="top:717px">For more than a decade, our Law Firm has been<br>providing skilled legal services to clients from<br>across the United States and around the world.</p>
    <div class="news__image news__image--papers" role="img" aria-label="Stack of newspapers resting on a laptop keyboard"></div>
    <p class="news__text" style="top:940px">For more than a decade, our Law Firm has been<br>providing skilled legal services to clients from<br>across the United States and around the world.</p>
    <a class="text-link" href="#" style="left:708px; top:1022px">More News</a>
  </section>

  <footer class="site-footer">
    <p><span class="copy">©</span>Brantley Legal PLLC | Attorney Advertising | Disclaimer</p>
  </footer>
</body>
</html>
```